Beautiful Customer Appreciation Gift Box Need Eye Catching Brochure

I need a brochure to include with small sample gift boxes that I send or give to companies who do door to door marketing of businesses, company reps, real estate designers and large companies looking for a unique customer appreciation gifts.

The brochure needs to capture the size variations and the limitless options for their budget and customization needs.

They are gift boxes that can be filled with cookies for the drug rep making an impression for the doc - after cookies are gone, the gift remains

At christmas, we fill them with baked goods and provide to each office. Every year as i visit the offices, they have last years gift box out as a decoration.

realtors can use them as a welcome to your new home gift filled with a bottle of wine and their papers left on the kitchen counter

We have had them used for baby shower gifts, kept later as a decoration.

that's the concept, i need it captured.
Marlow's Festive Nook is the current name
a tag line we came up with is It's all in the WRAPPINGS.
Updates

Project Deadline Extended
Reason: We are very close, I have my photoshoot tomorrow and I'd like to see and continue to tweek the current designs. I have pretty well deleted the designs we are not considering at this point. The others all have components we love. So I need a little more time and some tweaking to decide for sure.

Target Market(s)

the target is the company or individuals looking for gift giving options for clients and customers. From the door to door salesperson looking to make a splash or big impression to the large company looking for nice corporate gift ideas.

The concept of say goodbye to plain jane gift boxes that all look alike... Say goodbye to expensive gift wrap and bows that get thrown away in minutes.... and hello to a beautiful custom made gift box that will remain a decoration or keepsake box forever....

Industry/Entity Type

Retail

Font styles to use
Sans Serif
Script

Requirements
Must have
• IMPORTANT... I CAN and AM GETTING better pictures for the printing purposes. I'm looking more for the concept of the brochuure and layout design.
• I'd love to have it have some place holders for various pictures and descriptions - because each industry targets different people, I'd like to be able to change the front cover of the brochure with a picture of a box that targets that audience a little.
• For a real estate person... i might choose a beautiful centerpiece looking one... vs, the ob/gyn office, I might choose a baby one.
• I have some design skill, just 0 times and the programs have changed alot over the years, so this may go on to future work and a long design relationship as the company grows and changes. I do know photoshop and pagemaker from long ago so I should be able to drop in pics and text options. if we use compatible programs.
Nice to have
• would love to have some kind of background for the page - not just plain white background.
• i like angles and curves
Should not have
• boxy look.

```html
<!DOCTYPE html>
<html lang="en">
<head>
<meta charset="utf-8">
<title>Marlow's Festive Nook – Tri-fold Brochure</title>
<link rel="stylesheet" href="https://fonts.googleapis.com/css2?family=Oswald:wght@500;600&family=Roboto:wght@400;500;700&family=Arimo:wght@400;700&display=swap">
<style>
:root{
  --stage:#2a2a2a;
  --blue-deep:#7f9bcf;
  --blue-mid:#a3b8de;
  --blue-pale:#cfdaee;
  --sage:#dfe7dc;
  --sage-pale:#eef2ea;
  --heading-blue:#5b82bb;
  --ink:#2b2b2b;
  --ink-dark:#1f1f1f;
  --white:#ffffff;
}
*{margin:0;padding:0;box-sizing:border-box}
html,body{width:768px;height:1200px;overflow:hidden;background:var(--stage)}
body{position:relative;font-family:"Arimo",Arial,sans-serif;color:var(--ink)}

.sheet{position:absolute;left:58px;width:650px;overflow:hidden;box-shadow:0 0 6px rgba(0,0,0,.6)}
.sheet--outside{top:68px;height:508px}
.sheet--inside{top:624px;height:506px;background:linear-gradient(90deg,var(--blue-pale),var(--sage-pale) 55%,var(--blue-pale))}
.panel{position:absolute;top:0;height:100%}
.backdrop{position:absolute;inset:0;width:100%;height:100%}

/* outside: about */
.panel--about{left:0;width:220px;background:linear-gradient(180deg,var(--sage) 40%,var(--sage-pale))}
.about-photo{position:absolute;left:0;top:0;width:220px;height:222px;
  background:linear-gradient(180deg,#5f6660,#9da69c 60%,rgba(223,231,220,0));}
.about-title{position:absolute;top:244px;left:0;width:220px;text-align:center;
  font:500 16px/20px "Roboto",sans-serif;color:var(--heading-blue);letter-spacing:.3px}
.about-text{position:absolute;top:272px;left:28px;width:174px;font-size:11.4px;line-height:13.5px;text-align:justify;color:var(--ink)}

/* outside: contact */
.panel--contact{left:220px;width:210px;background:linear-gradient(90deg,var(--blue-deep),var(--blue-pale))}
.photo-ring{position:absolute;border-radius:50%;border:6px solid var(--white);box-shadow:0 1px 4px rgba(0,0,0,.35)}
.brand{position:absolute;font:500 14px/18px "Roboto",sans-serif;color:var(--ink-dark);white-space:nowrap}
.brand--contact{top:370px;left:0;width:210px;text-align:center}
.call-label{position:absolute;top:400px;left:0;width:210px;text-align:center;font:700 19px/22px "Roboto",sans-serif;color:var(--white)}
.call-number{position:absolute;top:425px;left:0;width:210px;text-align:center;font:700 22px/26px "Roboto",sans-serif;color:var(--ink-dark);letter-spacing:.5px}
.web{position:absolute;font:700 15px/18px "Roboto",sans-serif;color:var(--ink-dark);white-space:nowrap}
.web--contact{top:468px;left:0;width:210px;text-align:center}

/* outside: cover */
.panel--cover{left:430px;width:220px;background:var(--sage-pale)}
.brand--cover{top:46px;left:14px;color:var(--white);font-size:15px}
.cover-headline{position:absolute;top:78px;left:12px;font-family:"Oswald",sans-serif;font-weight:500;color:var(--white);text-shadow:0 1px 3px rgba(0,0,0,.35);line-height:1;white-space:nowrap}
.cover-headline span{display:block}
.cover-headline .l1{font-size:30px;margin-bottom:12px}
.cover-headline .l2{font-size:28px;margin-bottom:14px}
.cover-headline .l3{font-size:20px}
.cover-photo{position:absolute;left:24px;top:266px;width:196px;height:242px;border-radius:90px 0 0 0;
  background:radial-gradient(ellipse at 55% 45%,#8b6fd0,#6a5aa8 40%,#cfd6e6 70%,rgba(207,214,230,0))}

/* inside: left */
.panel--gallery{left:0;width:220px}
.brand--gallery{top:436px;left:0;width:220px;text-align:center}
.web--gallery{top:468px;left:0;width:220px;text-align:center;font-size:16px}

/* inside: feature */
.panel--feature{left:220px;width:430px}
.feature-headline{position:absolute;top:24px;left:0;width:430px;text-align:center;white-space:nowrap;font:500 26px/32px "Oswald",sans-serif;color:var(--white);text-shadow:0 1px 3px rgba(0,0,0,.35)}
.feature-intro{position:absolute;top:66px;left:22px;width:396px;font-size:9px;line-height:12px;color:var(--ink)}
.item{position:absolute;left:18px;width:412px;height:90px}
.item--band{background:linear-gradient(90deg,rgba(255,255,255,.55),rgba(255,255,255,.8));border-radius:45px 0 0 45px}
.item-title{position:absolute;top:12px;font:500 11.5px/14px "Oswald",sans-serif;color:var(--heading-blue);white-space:nowrap}
.item-text{position:absolute;top:29px;font-size:8px;line-height:11.2px;color:var(--ink);white-space:nowrap}
.item--left .item-title,.item--left .item-text{left:100px;width:306px}
.item--right .item-title,.item--right .item-text{left:6px;width:306px;text-align:right}
.item .photo-ring{top:2px;width:86px;height:86px;border-width:4px}
.item--left .photo-ring{left:8px}
.item--right .photo-ring{left:320px}
.item--violet .photo-ring{background:radial-gradient(circle,#8f7fc0,#8a5f3c 70%)}
.item--baby .photo-ring{background:radial-gradient(circle,#d7a6c8,#8a5f3c 70%)}
.item--pink .photo-ring{background:radial-gradient(circle,#e07ab0,#c9cfa8 70%)}
</style>
</head>
<body>

<section class="sheet sheet--outside">
  <div class="panel panel--about">
    <div class="about-photo" role="img" aria-label="Photo of floral holiday gift boxes, shown in greyscale"></div>
    <h2 class="about-title">ABOUT US</h2>
    <p class="about-text">Marlow's Festive Nook provides a range of holiday decorations. Most popular lines include the Christmas Holidays where you can choose your theme for a customized "Christmas Tree in a Box". New collections include the Spring Collection for celebrating Easter, Mother's Day, and Memorial Day. Garden and bird lovers are drawn to Marlow's signature brand. Doves and Cardinals along with hummingbirds ang butterflies are popular choices.</p>
  </div>

  <div class="panel panel--contact">
    <svg class="backdrop" viewBox="0 0 210 508" preserveAspectRatio="none" aria-hidden="true">
      <path d="M0 0 C40 40 30 200 120 300 C170 360 200 420 210 508 L196 508 C186 430 150 370 104 310 C20 200 28 50 0 10 Z" fill="#eef2ea" opacity=".8"/>
    </svg>
    <div class="photo-ring" style="left:-2px;top:38px;width:108px;height:108px;background:radial-gradient(circle,#d9a3c4,#8a6a4a 70%)" role="img" aria-label="Photo of a pink floral gift box"></div>
    <div class="photo-ring" style="left:34px;top:144px;width:108px;height:108px;background:radial-gradient(circle,#6f93c8,#7a5a36 70%)" role="img" aria-label="Photo of a blue daisy gift box"></div>
    <div class="photo-ring" style="left:96px;top:246px;width:114px;height:114px;background:radial-gradient(circle,#7a8a5a,#5a3e2a 70%)" role="img" aria-label="Photo of a woodland themed gift box"></div>
    <div class="brand brand--contact">Marlow's Festive Nook</div>
    <div class="call-label">CALL US TODAY</div>
    <div class="call-number">XXXXXXXXXX</div>
    <div class="web web--contact">marlowsfestivenook.com</div>
  </div>

  <div class="panel panel--cover">
    <svg class="backdrop" viewBox="0 0 220 508" preserveAspectRatio="none" aria-hidden="true">
      <defs>
        <linearGradient id="coverBlue" x1="0" y1="0" x2="1" y2="1">
          <stop offset="0" stop-color="#a9bde0"/><stop offset="1" stop-color="#7f9bcf"/>
        </linearGradient>
      </defs>
      <path d="M0 0 H220 V30 C150 60 110 180 70 300 C50 370 20 440 0 508 Z" fill="url(#coverBlue)"/>
      <path d="M220 24 C148 56 108 176 66 298 C46 366 18 438 0 500 L0 508 C22 442 52 372 74 302 C114 184 152 64 220 36 Z" fill="#ffffff"/>
      <circle cx="130" cy="372" r="100" fill="#9fb4dc"/>
    </svg>
    <div class="brand brand--cover">Marlow's Festive Nook</div>
    <h1 class="cover-headline"><span class="l1">LOREM IPSUM</span><span class="l2">INDUSTRY'S</span><span class="l3">DUMMY TEXT</span></h1>
    <div class="cover-photo" role="img" aria-label="Photo of a purple and white floral centerpiece gift box"></div>
  </div>
</section>

<section class="sheet sheet--inside">
  <div class="panel panel--gallery">
    <svg class="backdrop" viewBox="0 0 220 506" preserveAspectRatio="none" aria-hidden="true">
      <defs>
        <linearGradient id="galleryBlue" x1="0" y1="0" x2="1" y2="0">
          <stop offset="0" stop-color="#8ea8d6"/><stop offset="1" stop-color="#b9c9e6"/>
        </linearGradient>
      </defs>
      <rect width="220" height="506" fill="url(#galleryBlue)"/>
      <path d="M0 0 H220 V506 C200 420 120 300 60 180 C30 120 10 60 0 40 Z" fill="#dfe7dc" opacity=".85"/>
      <path d="M0 36 C14 70 34 126 62 182 C122 302 200 420 220 500 L220 506 C196 424 116 306 56 186 C28 130 10 76 0 48 Z" fill="#ffffff"/>
    </svg>
    <div class="photo-ring" style="left:16px;top:26px;width:108px;height:108px;background:radial-gradient(circle,#d8a6c8,#8a5f3c 70%)" role="img" aria-label="Photo of a baby themed gift box"></div>
    <div class="photo-ring" style="left:38px;top:156px;width:118px;height:118px;background:radial-gradient(circle,#e07ab0,#c9cfa8 70%)" role="img" aria-label="Photo of a pink floral baby gift box"></div>
    <div class="photo-ring" style="left:86px;top:286px;width:128px;height:128px;background:radial-gradient(circle,#5e5a9a,#8a5a30 70%)" role="img" aria-label="Photo of an open keepsake gift box with violets"></div>
    <div class="brand brand--gallery">Marlow's Festive Nook</div>
    <div class="web web--gallery">marlowsfestivenook.com</div>
  </div>

  <div class="panel panel--feature">
    <svg class="backdrop" viewBox="0 0 430 506" preserveAspectRatio="none" aria-hidden="true">
      <defs>
        <linearGradient id="featureBlue" x1="0" y1="0" x2="1" y2="0">
          <stop offset="0" stop-color="#8ea8d6"/><stop offset=".5" stop-color="#c9d6ec"/><stop offset="1" stop-color="#9fb4dc"/>
        </linearGradient>
      </defs>
      <rect width="430" height="506" fill="url(#featureBlue)"/>
      <path d="M0 506 C60 460 200 440 430 448 V506 Z" fill="#9fb4dc"/>
      <path d="M0 500 C70 456 210 436 430 444 V452 C210 446 80 464 8 506 Z" fill="#ffffff"/>
      <path d="M0 506 C100 470 260 462 430 470 V506 Z" fill="#eef2ea"/>
    </svg>
    <h2 class="feature-headline">LOREM IPSUM IS SIMPLY DUMMY TEXT</h2>
    <p class="feature-intro">Lorem Ipsum is simply dummy text of the printing and typesetting industry. Lorem Ipsum has been the industry's standard dummy text ever since the 1500s, when an unknown printer took a galley of type and scrambled it to make a type specimen book. It has survived not only five centuries, but also the leap into electronic typesetting, remaining essentially unchanged.</p>

    <article class="item item--band item--left item--violet" style="top:128px">
      <div class="photo-ring" role="img" aria-label="Photo of an open gift box with violets"></div>
      <h3 class="item-title">LOREM IPSUM IS SIMPLY DUMMY TEXT</h3>
      <p class="item-text">Lorem Ipsum is simply dummy text of the printing and typesetting industry.<br>Lorem Ipsum has been the industry's standard dummy text ever since the<br>1500s, when an unknown printer took a galley of type and scrambled it to<br>make a type specimen book. It has survived not only five centuries, but also<br>the leap into electronic typesetting, remaining essentially unchanged.</p>
    </article>

    <article class="item item--right item--baby" style="top:230px">
      <div class="photo-ring" role="img" aria-label="Photo of a baby themed gift box"></div>
      <h3 class="item-title">LOREM IPSUM IS SIMPLY DUMMY TEXT</h3>
      <p class="item-text">Lorem Ipsum is simply dummy text of the printing and typesetting industry.<br>Lorem Ipsum has been the industry's standard dummy text ever since the<br>1500s, when an unknown printer took a galley of type and scrambled it to<br>make a type specimen book. It has survived not only five centuries, but also<br>the leap into electronic typesetting, remaining essentially unchanged.</p>
    </article>

    <article class="item item--band item--left item--pink" style="top:330px">
      <div class="photo-ring" role="img" aria-label="Photo of a pink floral baby gift box"></div>
      <h3 class="item-title">LOREM IPSUM IS SIMPLY DUMMY TEXT</h3>
      <p class="item-text">Lorem Ipsum is simply dummy text of the printing and typesetting industry.<br>Lorem Ipsum has been the industry's standard dummy text ever since the<br>1500s, when an unknown printer took a galley of type and scrambled it to<br>make a type specimen book. It has survived not only five centuries, but also<br>the leap into electronic typesetting, remaining essentially unchanged.</p>
    </article>
  </div>
</section>
</body>
</html>
```